Corvant Systems Business Card

Create an appealing and elegant Business card for corvant systems. Include logo and use related colors from website, be creative. Include Business name, my name, tile, address, contacts, address, and social media contacts if possible. Logo PSD file is attached.

Bleed Area: 3.46" x 2.32"
Trim: 3.3" x 2.16"
Safe Area: 3.14" x 2.02"

Save files as vector-based PDF with outlined text and PNG.
No crop marks
CMYK color setting

Business Card Info:

Corvant Systems

Dennis Halvorsen
Owner

512 Brindlemoor Rd Unit C
Ashmere Falls, NH 02871
t. 1.888.555.0162
e. dennis.h@corvantsys.example
w. www.corvantsys.example

facebook. www.facebook.com/CorvantSys
twitter. twitter.com/corvantsys
pinterest. www.pinterest.com/corvantsys/

Target Market(s)

Business Owners and Partners

Industry/Entity Type

Business

Requirements
Must have
• Logo and related colors from website

```html
<!DOCTYPE html>
<html lang="en">
<head>
<meta charset="utf-8">
<title>Corvant Systems Business Card</title>
<link rel="stylesheet" href="https://fonts.googleapis.com/css2?family=Open+Sans:wght@400;600;700&display=swap">
<style>
  :root {
    --stage: #bbbcbe;
    --ink: #000000;
    --ink-soft: #07090b;
    --paper: #ffffff;
    --brand-blue: #4a73a8;
  }
  html, body {
    margin: 0;
    width: 1200px;
    height: 927px;
    overflow: hidden;
    background: var(--stage);
    font-family: "Open Sans", sans-serif;
  }
  .canvas { position: relative; width: 1200px; height: 927px; }
  .card {
    position: absolute;
    top: 111px;
    width: 426px;
    height: 709px;
    box-shadow: 8px 8px 12px rgba(0,0,0,0.35);
    overflow: hidden;
  }
  .card--front { left: 128px; background: var(--ink); }
  .card--back { left: 639px; background: var(--paper); }
  .side-strip { position: absolute; top: 0; bottom: 0; background: var(--ink); }
  .card--back .side-strip--left { left: 0; width: 31px; }
  .card--back .side-strip--right { right: 0; width: 34px; }

  .band { position: absolute; }
  .band--blue { background: var(--brand-blue); }
  .band--black { background: var(--ink-soft); }
  .band--white { background: var(--paper); }

  .logo-panel {
    position: absolute;
    left: 31px; top: 84px;
    width: 361px; height: 205px;
    background: var(--paper);
  }
  .wordmark {
    position: absolute;
    left: 0; right: 0;
    text-align: center;
    color: var(--ink);
    line-height: 1;
    margin: 0;
  }
  .wordmark span { display: block; }
  .wordmark .line-1 { font-size: 60px; font-weight: 700; letter-spacing: 1px; }
  .wordmark .line-2 { font-size: 48px; font-weight: 400; margin-top: 6px; }
  .logo-panel .wordmark { top: 38px; }
  .card--back .wordmark { top: 302px; left: 31px; right: 34px; }
  .card--back .wordmark .line-1 { font-size: 70px; }
  .card--back .wordmark .line-2 { font-size: 55px; margin-top: 4px; }

  .contact { position: absolute; left: 89px; top: 378px; color: var(--paper); }
  .contact__name { margin: 0; color: var(--brand-blue); font-weight: 700; font-size: 20px; line-height: 26px; }
  .contact__title { margin: 0; font-size: 15px; line-height: 20px; }
  .contact__list { margin: 34px 0 0; padding: 0; list-style: none; font-size: 15.5px; line-height: 23.5px; }
  .contact__list .label { display: inline-block; width: 23px; }
  .contact__address { margin: 0; font-size: 15.5px; line-height: 20.5px; font-style: normal; padding-top: 2px; }
</style>
</head>
<body>
<div class="canvas">

  <section class="card card--front" aria-label="Card front">
    <div class="band band--blue" style="left:31px;top:0;width:200px;height:84px"></div>
    <div class="band band--white" style="left:231px;top:0;width:10px;height:84px"></div>
    <div class="band band--black" style="left:241px;top:0;width:72px;height:84px"></div>
    <div class="band band--white" style="left:313px;top:0;width:10px;height:84px"></div>
    <div class="band band--blue" style="left:323px;top:0;width:69px;height:84px"></div>

    <div class="logo-panel">
      <h1 class="wordmark"><span class="line-1">CORVANT</span><span class="line-2">Systems</span></h1>
    </div>

    <div class="contact">
      <p class="contact__name">Dennis Halvorsen</p>
      <p class="contact__title">Owner</p>
      <ul class="contact__list">
        <li><span class="label">T.</span>1.888.555.0162</li>
        <li><span class="label">W.</span>www.corvantsys.example</li>
        <li><span class="label">E.</span>dennis.h@corvantsys.example</li>
      </ul>
      <address class="contact__address">512 Brindlemoor Rd Unit C<br>Ashmere Falls, NH 02871</address>
    </div>

    <div class="band band--white" style="left:31px;top:666px;width:361px;height:12px"></div>
    <div class="band band--blue" style="left:31px;top:678px;width:200px;height:31px"></div>
    <div class="band band--white" style="left:231px;top:678px;width:10px;height:31px"></div>
    <div class="band band--black" style="left:241px;top:678px;width:72px;height:31px"></div>
    <div class="band band--white" style="left:313px;top:678px;width:10px;height:31px"></div>
    <div class="band band--blue" style="left:323px;top:678px;width:69px;height:31px"></div>
  </section>

  <section class="card card--back" aria-label="Card back">
    <div class="side-strip side-strip--left"></div>
    <div class="side-strip side-strip--right"></div>

    <div class="band band--blue" style="left:31px;top:0;width:200px;height:84px"></div>
    <div class="band band--black" style="left:241px;top:0;width:72px;height:84px"></div>
    <div class="band band--blue" style="left:323px;top:0;width:69px;height:84px"></div>

    <h2 class="wordmark"><span class="line-1">CORVANT</span><span class="line-2">Systems</span></h2>

    <div class="band band--blue" style="left:31px;top:624px;width:200px;height:85px"></div>
    <div class="band band--black" style="left:241px;top:624px;width:72px;height:85px"></div>
    <div class="band band--blue" style="left:323px;top:624px;width:69px;height:85px"></div>
  </section>

</div>
</body>
</html>
```